Premium Nail Dip Powder Label Design

We need a label design for a 2 ounce jar in which we will be selling our new product line of dip powder to nail salons. For reference, please see competitors' products that are currently selling in the market. The label size is 16cm long by 2.5cm wide. We have a logo design that is attached - the "drop" should be in shiny gold (metallic). This label will wrap around the round jar and the first half will be the "front" and the second half will be the "back". Please see the attached writing that will be required for the second half, or "back" part of the label.

Target Market(s)

Retail Nail Salons in the US

Font styles to use
Sans Serif

Colors

Designer to choose colors to be used in the design.

Requirements
Must have
• "RVT" logo with the "drop" in shiny/metallic gold to match the shiny gold lid that we will have for it. The words "Premium Dip Powder". The size "2 oz". The wording for the second half, or "back" part of the label attached should be in black color with the size adjusted to fit the label size.
Nice to have
• different designs of fonts and sizes and colors for "Premium Dip Powder" which should be on the "front" of the label under our logo.

```html
<!DOCTYPE html>
<html lang="en">
<head>
<meta charset="utf-8">
<title>RVT Premium Dip Powder – Jar Label</title>
<link rel="stylesheet" href="https://fonts.googleapis.com/css2?family=Montserrat:wght@300;400;600&family=Arimo:wght@400;700&display=swap">
<style>
  :root {
    --page: #ffffff;
    --pink: #ff5f92;
    --pink-light: #ff86b0;
    --pink-deep: #f3487f;
    --blush: #ffe6ee;
    --gold: #d9a94b;
    --band-light: #f6c6a4;
    --band-mid: #e89a66;
    --band-deep: #c8683f;
    --white: #ffffff;
  }
  * { box-sizing: border-box; margin: 0; padding: 0; }
  html, body { width: 1200px; height: 1200px; overflow: hidden; background: var(--page); }
  .canvas {
    width: 1200px; height: 1200px;
    display: flex; align-items: center; justify-content: center;
  }
  .label {
    display: flex;
    width: 1140px; height: 370px;
    background: linear-gradient(90deg, var(--pink-deep), var(--pink-light) 25%, var(--pink) 50%, var(--pink-light) 75%, var(--pink-deep));
  }
  .panel { position: relative; width: 570px; height: 100%; }
  .band {
    position: absolute; left: 0; right: 0;
    background: linear-gradient(90deg, var(--band-light), var(--band-mid) 30%, var(--band-deep) 55%, var(--band-mid) 75%, var(--band-light));
  }

  /* front */
  .brand {
    position: absolute; top: 48px; left: 0; right: 0;
    display: flex; align-items: center; justify-content: center; gap: 18px;
  }
  .brand-name {
    font-family: "Montserrat", sans-serif; font-weight: 600;
    font-size: 140px; line-height: 1; letter-spacing: -4px;
    color: var(--blush);
  }
  .brand-dot { width: 44px; height: 44px; border-radius: 50%; background: var(--gold); }
  .front .band { top: 192px; height: 104px; }
  .product-name {
    position: absolute; top: 200px; left: 75px; right: 45px;
    font-family: "Montserrat", sans-serif; font-weight: 300;
    color: var(--blush); text-align: center; letter-spacing: 3px;
  }
  .product-name .line1 { font-size: 40px; line-height: 44px; }
  .product-name .rule { height: 2px; background: var(--blush); margin: 0 0 2px; }
  .product-name .line2 { font-size: 40px; line-height: 44px; }
  .net-weight {
    position: absolute; top: 312px; left: 0; right: 0; text-align: center;
    font-family: "Arimo", sans-serif; font-size: 18px; color: var(--white);
  }

  /* back */
  .back-copy {
    position: absolute; left: 100px; right: 40px;
    font-family: "Arimo", sans-serif; color: var(--white);
  }
  .usage { top: 58px; font-size: 16px; line-height: 20px; }
  .usage strong { font-weight: 700; display: block; margin-bottom: 19px; }
  .back .band { top: 196px; height: 104px; }
  .ingredients { top: 204px; left: 94px; font-size: 16px; line-height: 20px; }
  .ingredients strong { font-weight: 700; display: block; }
  .maker {
    position: absolute; top: 318px; left: 0; right: 0; text-align: center;
    font-family: "Arimo", sans-serif; font-size: 12px; line-height: 16px; color: var(--white);
  }
</style>
</head>
<body>
<main class="canvas">
  <section class="label">
    <div class="panel front">
      <div class="brand">
        <span class="brand-name">RVT</span>
        <span class="brand-dot"></span>
      </div>
      <div class="band"></div>
      <div class="product-name">
        <div class="line1">PREMIUM</div>
        <div class="rule"></div>
        <div class="line2">DIP POWDER</div>
      </div>
      <p class="net-weight">Net Wt. 2 oz</p>
    </div>
    <div class="panel back">
      <div class="back-copy usage">
        <strong>For Use By Nail Professionals Only</strong>
        CAUTION: KEEP OUT OF REACH OF CHILDREN.<br>
        Keep away from heat, humidity and sunlight.<br>
        Discontinue use if sensitivity or irritation occurs.
      </div>
      <div class="band"></div>
      <div class="back-copy ingredients">
        <strong>INGREDIENTS:</strong>
        Polyethylmethacrylate, Acrylates Copolymer, Benzoyl Peroxide and PEG-12 Dimethicone. May also contain various coloring agents and glitters.
      </div>
      <p class="maker">Manufactured Exclusively For: Bluewave Trading, Inc., USA<br>www.bluewavetrading.com</p>
    </div>
  </section>
</main>
</body>
</html>
```